Over 100 ladies will be traveling to Ocean City, MD for a Women's Retreat Conference. This flyer is for advertisement. This flyer is to circulate for registrations as well as to post on social media. Theme is Holy Spirit fire. I have attached a photo. All the information in the attachment should be included on the flyer. Information should be clearly readable end eye catching.

Target Market(s)

Church ladies

Industry/Entity Type

Religious

Font styles to use
Sans Serif

Colors

Designer to choose colors to be used in the design.

Requirements
Must have
• Title: Tidewell Womens Retreat 2019 "FIRE"
• All components in attachments

```html
<!DOCTYPE html>
<html lang="en">
<head>
<meta charset="utf-8">
<title>Tidewell Womens Retreat 2019 "FIRE"</title>
<link rel="stylesheet" href="https://fonts.googleapis.com/css2?family=Bebas+Neue&family=Lato:wght@400;700&family=Oswald:wght@500;600&display=swap">
<style>
  :root {
    --page-bg: #f2f2f2;
    --paper: #ffffff;
    --ink: #1a1a1a;
    --red: #cf1f1a;
    --plum: #7c1a6f;
    --plum-deep: #5e1763;
    --magenta: #d61a7b;
    --band: #e6e6e6;
    --white: #ffffff;
  }
  * { box-sizing: border-box; margin: 0; padding: 0; }
  html, body { width: 1200px; height: 1200px; overflow: hidden; background: var(--page-bg); }
  .stage { position: relative; width: 1200px; height: 1200px; }
  .flyer {
    position: absolute; left: 172px; top: 0;
    width: 823px; height: 1155px;
    transform: scale(1.039); transform-origin: top left;
    background: var(--paper); overflow: hidden;
    font-family: "Lato", sans-serif; color: var(--ink);
  }
  .backdrop { position: absolute; inset: 0; }
  .abs { position: absolute; }

  .venue-name {
    left: 38px; top: 34px; font-weight: 700; font-size: 25px; color: var(--plum);
    padding-bottom: 2px; border-bottom: 3px solid var(--plum); width: 383px;
    white-space: nowrap; letter-spacing: -0.2px;
  }
  .venue-address { left: 38px; top: 74px; font-size: 24px; line-height: 30px; white-space: nowrap; }

  .title { left: 30px; top: 160px; font-family: "Bebas Neue", sans-serif; line-height: 1; }
  .title-name { color: var(--red); font-size: 104px; display: block; height: 92px; }
  .title-line { color: var(--plum); font-size: 82px; display: block; height: 80px; }
  .title-fire { color: var(--red); }

  .included-tag {
    left: 0; top: 466px; width: 206px; height: 52px; background: var(--red);
    border-radius: 0 26px 26px 0; color: var(--white);
    font-family: "Oswald", sans-serif; font-weight: 500; font-size: 34px;
    display: flex; align-items: center; padding-left: 44px; letter-spacing: 0.5px;
  }
  .included-list { left: 30px; top: 536px; list-style: none; font-size: 21px; }
  .included-list li { height: 35px; display: flex; align-items: center; gap: 6px; }
  .included-list svg { width: 15px; height: 15px; flex: none; }

  .cost-pill {
    left: 25px; top: 710px; width: 338px; height: 86px; background: var(--red);
    border-radius: 26px; color: var(--white);
    font-family: "Bebas Neue", sans-serif; font-size: 82px; line-height: 86px; padding-left: 32px;
  }
  .cost-note { left: 65px; top: 804px; font-size: 18px; }

  .terms { left: 30px; top: 876px; width: 410px; color: var(--white); font-size: 15.6px; line-height: 19.5px; }
  .terms b { font-weight: 700; }
  .contact { margin-top: 4px; white-space: nowrap; }
  .website { left: 32px; top: 1072px; color: var(--white); font-size: 24px; display: flex; align-items: center; gap: 14px; }
  .website svg { width: 36px; height: 36px; }

  .section-label {
    color: var(--white); font-family: "Oswald", sans-serif; font-weight: 600;
    font-size: 28px; letter-spacing: -0.5px; transform: scaleX(0.85); transform-origin: left;
  }
  .host-label { left: 553px; top: 183px; }
  .speakers-label { left: 548px; top: 604px; }

  .portrait { width: 170px; height: 170px; border-radius: 50%; border: 3px solid var(--white); }
  .portrait-host { left: 613px; top: 263px; background: radial-gradient(circle at 50% 45%, #c98a5f 0%, #8a4a2e 45%, #e6d8cf 75%); }
  .portrait-one { left: 613px; top: 655px; background: radial-gradient(circle at 40% 50%, #5a3a2c 0%, #2a2222 50%, #c9c4c0 80%); }
  .portrait-two { left: 613px; top: 903px; background: radial-gradient(circle at 50% 45%, #4a2e24 0%, #1c1b1d 55%, #f0f0f0 80%); }

  .name-card {
    left: 554px; width: 163px; background: var(--white); color: var(--ink);
    font-family: "Oswald", sans-serif; font-weight: 500; font-size: 15px; line-height: 20px;
    padding: 0 12px; display: flex; flex-direction: column; justify-content: center;
  }
  .name-card span { display: block; transform: scaleX(0.82); transform-origin: left; white-space: nowrap; }
  .card-host { top: 435px; height: 55px; }
  .card-one { top: 829px; height: 56px; }
  .card-two { top: 1077px; height: 54px; }
</style>
</head>
<body>
<div class="stage">
  <article class="flyer">
    <svg class="backdrop" viewBox="0 0 823 1155" width="823" height="1155" aria-hidden="true">
      <defs>
        <linearGradient id="plumGrad" x1="0" y1="0" x2="0.3" y2="1">
          <stop offset="0" stop-color="#651a6a"/>
          <stop offset="0.45" stop-color="#b51a7b"/>
          <stop offset="0.7" stop-color="#d61a7b"/>
          <stop offset="1" stop-color="#6e1a6c"/>
        </linearGradient>
        <linearGradient id="fireGrad" x1="0" y1="0" x2="0" y2="1">
          <stop offset="0" stop-color="#c9250f"/>
          <stop offset="0.45" stop-color="#b8230e"/>
          <stop offset="0.75" stop-color="#e2571a"/>
          <stop offset="1" stop-color="#f08a2a"/>
        </linearGradient>
      </defs>
      <polygon points="0,462 488,102 540,215 0,540" fill="var(--band)"/>
      <polygon class="plum-panel" points="557,0 823,0 823,1155 400,1155 400,865 568,365 488,100" fill="url(#plumGrad)"/>
      <polygon points="488,100 823,360 823,440 650,600 568,365" fill="#5e1763" opacity="0.45"/>
      <polygon points="650,600 823,440 823,1155 700,1155" fill="#7a1a6e" opacity="0.35"/>
      <polygon points="400,865 650,600 823,700 823,800" fill="#e21f7d" opacity="0.25"/>
      <polygon points="540,1155 650,1040 823,1155" fill="#f01d7f" opacity="0.6"/>
      <polygon class="fire-block" role="img" aria-label="Flames rising along the bottom edge" points="0,865 400,865 540,1155 0,1155" fill="url(#fireGrad)"/>
    </svg>

    <p class="abs venue-name">SANDCREST HOTEL &amp; SUITES</p>
    <p class="abs venue-address">1450 Seabreeze Ave.<br>Ocean City, Maryland 21842</p>

    <h1 class="abs title">
      <span class="title-name">TIDEWELL</span>
      <span class="title-line">WOMENS RETREAT</span>
      <span class="title-line">2019 <span class="title-fire">"FIRE"</span></span>
    </h1>

    <div class="abs included-tag">Included</div>
    <ul class="abs included-list">
      <li><svg viewBox="0 0 16 16"><circle cx="8" cy="8" r="6.5" fill="none" stroke="#7c1a6f" stroke-width="1.3"/><path d="M6.5 5l3 3-3 3" fill="none" stroke="#7c1a6f" stroke-width="1.6"/></svg>All Retreat Sessions</li>
      <li><svg viewBox="0 0 16 16"><circle cx="8" cy="8" r="6.5" fill="none" stroke="#7c1a6f" stroke-width="1.3"/><path d="M6.5 5l3 3-3 3" fill="none" stroke="#7c1a6f" stroke-width="1.6"/></svg>2 Nights Hotel Accommodations</li>
      <li><svg viewBox="0 0 16 16"><circle cx="8" cy="8" r="6.5" fill="none" stroke="#7c1a6f" stroke-width="1.3"/><path d="M6.5 5l3 3-3 3" fill="none" stroke="#7c1a6f" stroke-width="1.6"/></svg>1 Hot Lunch Buffet</li>
      <li><svg viewBox="0 0 16 16"><circle cx="8" cy="8" r="6.5" fill="none" stroke="#7c1a6f" stroke-width="1.3"/><path d="M6.5 5l3 3-3 3" fill="none" stroke="#7c1a6f" stroke-width="1.6"/></svg>1 Full Hot American Breakfast</li>
    </ul>

    <div class="abs cost-pill">COST:$295</div>
    <p class="abs cost-note">*Based on double occupancy</p>

    <div class="abs terms">
      <p>**ALL deposits/registrations are NON-refundable and NON-transferable. Your entire registration is due by October 1, 2018. Please submit your desired roommate's name at the time of registration. If you do not choose a roommate one will be assigned to you unless you have registered for a private room.</p>
      <p class="contact">Please contact <b>Marisol</b> via email <b>marisol@whitfieldministries.org</b><br>or phone <b>240-555-0187</b> for more information.</p>
    </div>
    <p class="abs website">
      <svg viewBox="0 0 36 36" aria-hidden="true"><g fill="none" stroke="#fff" stroke-width="2"><circle cx="18" cy="18" r="15"/><ellipse cx="18" cy="18" rx="7" ry="15"/><line x1="3" y1="18" x2="33" y2="18"/><path d="M6 10h24M6 26h24"/></g></svg>
      tidewell2019.eventsite.com
    </p>

    <h2 class="abs section-label host-label">RETREAT HOST:</h2>
    <div class="abs portrait portrait-host" role="img" aria-label="Portrait photo of the retreat host"></div>
    <div class="abs name-card card-host"><span>APOSTLE LOREEN WHITFIELD</span></div>

    <h2 class="abs section-label speakers-label">RETREAT SPEAKERS :</h2>
    <div class="abs portrait portrait-one" role="img" aria-label="Portrait photo of the first retreat speaker"></div>
    <div class="abs name-card card-one"><span>PASTOR DANETTE MOORE</span><span>ORLANDO, FLORIDA</span></div>
    <div class="abs portrait portrait-two" role="img" aria-label="Portrait photo of the second retreat speaker"></div>
    <div class="abs name-card card-two"><span>PASTOR CELESTE GRANT</span><span>- HLCM - WALDORF, MD.</span></div>
  </article>
</div>
</body>
</html>
```